People Search Directory Needs a Web Design

We need a web design for a new web site called Kestrel Lineage Lookups. We provide free directory information, such as name, phone, address, and email. We also provide other non-white pages information such as the person's relatives, historical records to help identify the person, and link the data so people can find connections. For example, by clicking on an address that a person lives at, you can find other people who might currently (or previously) have lived at that address.

We have a very basic web page that contains a lot of public records data. The page can look very busy. We need it to be concise, where the white pages type of information is easily identifiable, but people also realize the usefulness of the surrounding data (such as possible relatives, email address, historical phone numbers, etc).

The web page also promotes an annual membership to get more in-depth information on people. These Kestrel Lineage Lookups include a criminal records check, property records, and other information.

Industry/Entity Type

Property

Requirements
Must have
• Attached is an example design we put together. We want the design to be snazzier, have more information architecture thought put into it, etc.

```html
<!DOCTYPE html>
<html lang="en">
<head>
<meta charset="utf-8">
<title>Kestrel Lineage Lookups</title>
<link rel="stylesheet" href="https://fonts.googleapis.com/css2?family=Ubuntu:wght@500;700&family=Arimo:wght@400;700&display=swap">
<style>
:root{
  --page:#e4e4e4;
  --panel:#ececec;
  --panel-edge:#c9c9c9;
  --brand:#1f6b9e;
  --band:#3aa6e2;
  --tab:#5ab4cb;
  --ink:#333;
  --muted:#777;
  --name:#2c6fad;
  --btn-grey:#c3bfbf;
  --sky:#31bdf2;
  --orange-top:#ff6f1f;
  --orange-bot:#c22a00;
  --green-top:#8fd11e;
  --green-bot:#4f9a07;
  --tick:#7cc21a;
  --field:#f7f7f7;
  --field-edge:#d3d3d3;
}
*{box-sizing:border-box;margin:0;padding:0}
html,body{width:1200px;height:880px;overflow:hidden}
body{background:linear-gradient(#ebebeb,#dedede);font-family:"Arimo",Arial,sans-serif;color:var(--ink);position:relative}
.abs{position:absolute}
.brand{left:64px;top:54px;font-family:"Ubuntu",sans-serif;font-weight:700;font-size:38px;color:var(--brand);letter-spacing:.6px;white-space:nowrap}
.brand-mark{left:578px;top:62px;width:26px;height:26px;background:var(--brand);border-radius:50%}
.tab{top:0;width:35px;height:89px;background:linear-gradient(#6cc2d7,var(--tab));display:flex;align-items:flex-end;justify-content:center;padding-bottom:14px;box-shadow:0 2px 4px rgba(0,0,0,.15)}
.tab.home{left:786px}.tab.mail{left:840px}
.site-search{left:901px;top:61px;width:245px;height:29px;background:#f1f1f1;border:1px solid #ccc;border-radius:2px;box-shadow:inset 0 1px 3px rgba(0,0,0,.08)}
.site-search svg{position:absolute;right:2px;top:-8px}
.date{left:786px;top:111px;font-size:13px;font-weight:700;color:#888;letter-spacing:.3px}
.band{left:0;top:145px;width:1200px;height:10px;background:linear-gradient(#52b4ea,#2f96d4)}
.panel{left:39px;top:163px;width:1123px;height:639px;background:linear-gradient(#f1f1f1,var(--panel));border:1px solid var(--panel-edge);box-shadow:inset 0 0 0 3px #fff,0 2px 6px rgba(0,0,0,.08)}
.label{left:180px;font-size:13px;font-weight:700;color:#444;letter-spacing:.3px}
.field{left:305px;width:163px;height:48px;background:var(--field);border:1px solid var(--field-edge);border-radius:5px;box-shadow:inset 0 1px 3px rgba(0,0,0,.06)}
.field.short{width:88px}
.select-arrow{position:absolute;right:10px;top:14px;width:16px;height:18px;border:1px solid #555;background:#eee}
.select-arrow::after{content:"";position:absolute;left:3px;top:6px;border:4px solid transparent;border-top:5px solid #222}
.search-btn{left:369px;top:485px;width:98px;height:52px;border-radius:22px;background:linear-gradient(var(--orange-top),var(--orange-bot));color:#fff;font-weight:700;font-size:17px;display:flex;align-items:center;justify-content:center;letter-spacing:.5px;box-shadow:0 3px 6px rgba(194,42,0,.3)}
.chevron{left:520px;top:218px}
.person-name{left:754px;top:198px;font-size:18px;font-weight:700;color:var(--name);letter-spacing:.5px}
.age{left:1020px;top:198px;font-size:17px;font-weight:700}
.age span{font-weight:400;font-size:15px;margin-left:8px}
.k{left:754px;font-size:14px;font-weight:700;letter-spacing:.3px}
.colon{left:834px;font-size:14px}
.v{left:852px;font-size:14px;line-height:20px;white-space:nowrap}
.v.link{color:var(--name);text-decoration:underline}
.v .note{color:var(--muted);font-size:12px;text-decoration:none;margin-left:6px}
.action{left:635px;width:511px;height:42px;background:linear-gradient(#cbc7c7,var(--btn-grey));border-radius:5px;font-size:15px;font-weight:700;color:#111;display:flex;align-items:center;justify-content:center;letter-spacing:.3px;box-shadow:0 2px 3px rgba(0,0,0,.1)}
.mini{top:514px;height:22px;background:var(--sky);color:#fff;font-weight:700;display:flex;align-items:center;justify-content:center}
.mini.map{left:886px;width:122px;font-size:14px;letter-spacing:.5px}
.mini.more{left:1037px;width:93px;font-size:13px}
.divider{left:57px;top:564px;width:1099px;height:1px;background:#d6d6d6}
.promo{left:76px;top:598px;width:1050px;height:168px;background:#fff;border-radius:6px;box-shadow:0 1px 4px rgba(0,0,0,.06)}
.promo-tab{left:539px;top:586px;width:568px;height:20px;background:#fff}
.follow{left:93px;top:644px;font-size:26px;color:#666;letter-spacing:1.5px}
.social{top:639px;width:40px;height:40px;background:#dcdcdc;border-radius:6px;font-size:10px;font-weight:700;color:#5a3a36;display:flex;align-items:center;justify-content:center}
.report-art{left:543px;top:592px;width:73px;height:70px;background:linear-gradient(135deg,#e9e9e2,#9aa39a);border-radius:4px;transform:rotate(-8deg)}
.promo-title{left:629px;top:594px;font-size:17px;font-weight:700;color:#222}
.promo-title span{color:var(--name)}
.perk{font-size:15px;color:#444;display:flex;align-items:center;gap:9px}
.perk svg{flex:none}
.get-btn{left:629px;top:716px;width:309px;height:27px;border-radius:3px;background:linear-gradient(var(--green-top),var(--green-bot));border:1px solid #4a8a0a;color:#fff;font-weight:700;font-size:14px;display:flex;align-items:center;justify-content:center}
.copyright{left:0;top:838px;width:1200px;text-align:center;font-size:13px;color:#555;letter-spacing:.5px}
</style>
</head>
<body>
<header>
  <div class="abs brand">Kestrel Lineage Lookups</div>
  <div class="abs brand-mark"></div>
  <div class="abs tab home"><svg width="18" height="16" viewBox="0 0 18 16"><path d="M9 1 1 8h2.5v7h4v-4h3v4h4V8H17z" fill="#fff"/></svg></div>
  <div class="abs tab mail"><svg width="18" height="14" viewBox="0 0 18 14"><rect x="1" y="1" width="16" height="12" fill="#fff"/><path d="M1 1l8 7 8-7" fill="none" stroke="#5ab4cb" stroke-width="1.6"/></svg></div>
  <div class="abs site-search"><svg width="40" height="40" viewBox="0 0 40 40"><circle cx="16" cy="16" r="10" fill="#dfeaf2" stroke="#8a9aa6" stroke-width="3"/><path d="M23 23l11 11" stroke="#555" stroke-width="5" stroke-linecap="round"/></svg></div>
  <div class="abs date">Sunday, January 22, 2012 12:31</div>
  <div class="abs band"></div>
</header>

<main class="abs panel"></main>

<section class="search-form">
  <div class="abs label" style="top:216px">First Name</div>
  <div class="abs field" style="top:200px"></div>
  <div class="abs label" style="top:269px">M.I</div>
  <div class="abs field short" style="top:253px"></div>
  <div class="abs label" style="top:321px">Last Name</div>
  <div class="abs field" style="top:305px"></div>
  <div class="abs label" style="top:374px">City</div>
  <div class="abs field" style="top:358px"></div>
  <div class="abs label" style="top:427px">State</div>
  <div class="abs field" style="top:411px"><span class="select-arrow"></span></div>
  <div class="abs search-btn">Search</div>
</section>

<svg class="abs chevron" width="120" height="230" viewBox="0 0 120 230"><path d="M2 2 113 93 13 222 105 93z" fill="#fff"/></svg>

<section class="person">
  <div class="abs person-name">Marcus Ellwood</div>
  <div class="abs age">Age<span>45</span></div>
  <div class="abs k" style="top:228px">Phone</div><div class="abs colon" style="top:228px">;</div>
  <div class="abs v" style="top:226px">58417 302198 <span class="note">prev. 58417 110943</span></div>
  <div class="abs k" style="top:258px">address</div><div class="abs colon" style="top:258px">:</div>
  <div class="abs v link" style="top:248px">42 Fenwick st<br>Brookvale&nbsp; NY&nbsp; 12845</div>
  <div class="abs k" style="top:298px">Email</div><div class="abs colon" style="top:298px">:</div>
  <div class="abs v" style="top:296px">hello@mailnest.com<br>contact@mailnest.com</div>
  <div class="abs k" style="top:342px">Relatives</div><div class="abs colon" style="top:342px">:</div>
  <div class="abs v link" style="top:340px">Ada Ellwood, Owen Ellwood</div>
  <div class="abs k" style="top:364px">History</div><div class="abs colon" style="top:364px">:</div>
  <div class="abs v link" style="top:362px">9 Lark ln, Brookvale NY <span class="note">2001–2009</span></div>
  <div class="abs action" style="top:400px">Check National Criminal Records for Rosalind T Harrow</div>
  <div class="abs action" style="top:450px">Advanced Background Report on Rosalind T Harrow</div>
  <div class="abs mini map">View Map</div>
  <div class="abs mini more">READ MORE</div>
</section>

<div class="abs divider"></div>

<section class="promo-area">
  <div class="abs promo"></div>
  <div class="abs promo-tab"></div>
  <div class="abs follow">Follow US</div>
  <div class="abs social" style="left:254px">Wren</div>
  <div class="abs social" style="left:314px">Plaza</div>
  <div class="abs social" style="left:374px">Guild</div>
  <div class="abs report-art" role="img" aria-label="Folded printed background report"></div>
  <div class="abs promo-title">Want more in-depth information on <span>Rosalind T Harrow</span>?</div>
  <div class="abs perk" style="left:629px;top:628px"><svg width="18" height="15" viewBox="0 0 18 15"><path d="M1 8l5 5L17 1" fill="none" stroke="#7cc21a" stroke-width="3.5"/></svg>Name and AKAs</div>
  <div class="abs perk" style="left:629px;top:652px"><svg width="18" height="15" viewBox="0 0 18 15"><path d="M1 8l5 5L17 1" fill="none" stroke="#7cc21a" stroke-width="3.5"/></svg>Up to 40-year address history</div>
  <div class="abs perk" style="left:629px;top:676px"><svg width="18" height="15" viewBox="0 0 18 15"><path d="M1 8l5 5L17 1" fill="none" stroke="#7cc21a" stroke-width="3.5"/></svg>Date of birth</div>
  <div class="abs perk" style="left:887px;top:628px"><svg width="18" height="15" viewBox="0 0 18 15"><path d="M1 8l5 5L17 1" fill="none" stroke="#7cc21a" stroke-width="3.5"/></svg>Evictions &amp; bankruptcies</div>
  <div class="abs perk" style="left:887px;top:652px"><svg width="18" height="15" viewBox="0 0 18 15"><path d="M1 8l5 5L17 1" fill="none" stroke="#7cc21a" stroke-width="3.5"/></svg>Property records</div>
  <div class="abs perk" style="left:887px;top:676px"><svg width="18" height="15" viewBox="0 0 18 15"><path d="M1 8l5 5L17 1" fill="none" stroke="#7cc21a" stroke-width="3.5"/></svg>Criminal records check</div>
  <div class="abs get-btn">Get advanced background report...</div>
</section>

<footer class="abs copyright">COPYRIGHT © 2012 XXXXXXX</footer>
</body>
</html>
```